Yard Sign Design Needed

Yard sign needed for mowing & landscaping company. Would like to use the top logo with black background which is attached. Would like MOWING to be in large standout letters. The word "landscaping" can be smaller and more artistic or omitted. Will need room for phone number once design is approved. The phone number will need to stand out and look identical/similar to the word 'MOWING"

```html
<!DOCTYPE html>
<html lang="en">
<head>
<meta charset="utf-8">
<title>Brennick Contractors – Mowing Yard Sign</title>
<link href="https://fonts.googleapis.com/css2?family=Poppins:wght@500;600&family=Roboto:wght@700&display=swap" rel="stylesheet">
<style>
  :root {
    --backdrop: #a4a4a4;
    --sign-white: #ffffff;
    --sign-black: #000000;
    --lime: #8fae12;
    --lime-bright: #9bbd16;
    --ink: #111111;
  }
  * { margin: 0; padding: 0; box-sizing: border-box; }
  html, body {
    width: 1200px;
    height: 780px;
    overflow: hidden;
    background: var(--backdrop);
  }
  .yard-sign {
    position: absolute;
    left: 105px;
    top: 20px;
    width: 990px;
    height: 740px;
    background: var(--sign-white);
  }
  .sign-shapes {
    position: absolute;
    inset: 0;
    width: 990px;
    height: 740px;
  }
  .brand-name {
    position: absolute;
    left: 0;
    right: 0;
    top: 200px;
    text-align: center;
    font-family: "Poppins", sans-serif;
    font-weight: 600;
    color: var(--lime-bright);
    line-height: 1;
  }
  .brand-name .brand-main {
    display: block;
    font-size: 54px;
    letter-spacing: 3px;
  }
  .brand-name .brand-sub {
    display: block;
    margin-top: 10px;
    font-size: 24px;
    letter-spacing: 2px;
  }
  .service-title {
    position: absolute;
    left: 0;
    right: 0;
    top: 365px;
    text-align: center;
    font-family: "Poppins", sans-serif;
    font-weight: 600;
    font-size: 98px;
    letter-spacing: 7px;
    line-height: 1;
    color: var(--sign-white);
  }
  .service-subtitle {
    position: absolute;
    left: 0;
    right: 0;
    top: 472px;
    text-align: center;
    font-family: "Poppins", sans-serif;
    font-weight: 500;
    font-size: 38px;
    line-height: 1;
    color: var(--sign-white);
  }
  .phone-number {
    position: absolute;
    left: 0;
    right: 0;
    top: 628px;
    text-align: center;
    font-family: "Roboto", sans-serif;
    font-weight: 700;
    font-size: 88px;
    letter-spacing: 1px;
    line-height: 1;
    color: var(--ink);
  }
</style>
</head>
<body>
  <div class="yard-sign">
    <svg class="sign-shapes" viewBox="0 0 990 740" aria-hidden="true">
      <path class="swoosh-shadow" d="M70,522 Q520,668 978,505 V572 Q540,680 70,522 Z" fill="var(--sign-black)"/>
      <path class="swoosh-lime" d="M70,522 Q520,660 978,498 V556 Q540,668 70,522 Z" fill="var(--lime)"/>
      <path class="black-panel" d="M12,12 H978 V516 Q540,642 12,503 Z" fill="var(--sign-black)"/>
    </svg>

    <div class="brand-name">
      <span class="brand-main">BRENNICK</span>
      <span class="brand-sub">CONTRACTORS LLC</span>
    </div>

    <h1 class="service-title">MOWING</h1>
    <p class="service-subtitle">landscaping</p>

    <p class="phone-number">555-019-4827</p>
  </div>
</body>
</html>
```